Fahrzeugbeschriftung Maler und Lackierer Blauer Rasko 318
Sehr gute Umsetzung des Projekts. Bin sehr zufrieden. Viele Grüße
Zielgruppe
Maler und Lackierer Firma
Aufgabenstellung
Ich habe einen Atlantisblauen Rasko 318 Lang Kasten ohne Fenster mit Heckklappe.
Hätte gerne eine sehr große Folierung, mein Logo ist sehr breit und hoch aber nicht füllig. Daher eventuell die zwei L''so groß gezogen das es über meinen Namens Schriftzug passt und es fülliger wird oder andere Vorschläge.
Außerdem würde es mir gefallen wenn es eine große weiße Fläche gibt, zb. Eine Farbwalze die dem Kasten einen weißen Anstrich verpasst auf dem dann das Logo und alles kommt.
Slogan; Qualität die man sehen kann.
Ausführende arbeiten:
Maler und Lackierarbeiten, Bodenbelagsarbeiten, Stuckateurarbeiten,
Tapezierarbeiten
Farben: Hellblau, Gelb, Pink, Rot
Info@teodor-fink.de
Kerbweg 9
70899 Tannbach

```html
<!DOCTYPE html>
<html lang="de">
<head>
<meta charset="utf-8">
<title>Teodor Fink – Fahrzeugbeschriftung</title>
<link rel="stylesheet" href="https://fonts.googleapis.com/css2?family=Marcellus&family=Noto+Serif:wght@400&display=swap">
<style>
  :root {
    --paper: #f5f6f8;
    --ink: #1b1b1b;
    --navy: #16236b;
    --navy-light: #2a3a86;
    --white: #ffffff;
    --panel-grey: #ececee;
    --cyan: #29c6df;
    --pink: #e8329b;
    --red: #e8323c;
    --yellow: #f7c82b;
    --violet: #b04fe0;
  }
  * { margin: 0; padding: 0; box-sizing: border-box; }
  html, body { width: 917px; height: 1200px; overflow: hidden; background: var(--paper); }
  body { position: relative; font-family: "Noto Serif", Georgia, serif; color: var(--ink); }

  .brand { position: absolute; text-align: center; }
  .brand-name { font-family: "Marcellus", "Times New Roman", serif; line-height: 1; letter-spacing: 1px; color: var(--ink); }
  .brand-tagline { display: flex; align-items: center; justify-content: center; gap: 6px; letter-spacing: 4px; }
  .brand-tagline .rule { height: 3px; background: var(--ink); }

  .header-brand { left: 0; width: 917px; top: 108px; }
  .header-brand .brand-name { font-size: 42px; }
  .header-brand .brand-tagline { font-size: 15px; margin-top: 6px; }
  .header-brand .rule { width: 44px; }

  /* side panel */
  .side-panel { position: absolute; left: 30px; top: 232px; width: 857px; height: 280px; overflow: hidden; border-radius: 6px; background: var(--white); }
  .side-blue { position: absolute; left: 0; top: 0; width: 470px; height: 100%; background: var(--navy); }
  .side-brush { position: absolute; left: 440px; top: 0; width: 110px; height: 100%; background: linear-gradient(90deg, var(--navy) 0%, var(--navy-light) 45%, var(--white) 100%); }
  .side-drips { position: absolute; left: 220px; top: 120px; width: 180px; height: 34px; border-radius: 3px 3px 14px 14px; background: linear-gradient(90deg, var(--cyan), var(--violet), var(--pink), var(--red), var(--yellow)); }
  .side-contact { position: absolute; left: 232px; top: 228px; display: flex; gap: 12px; color: var(--white); font-size: 13px; line-height: 1.3; }
  .side-brand { position: absolute; left: 686px; top: 30px; text-align: left; }
  .side-brand .brand-name { font-size: 30px; line-height: 1.05; }
  .side-mark { position: absolute; left: 634px; top: 36px; width: 40px; height: 40px; background: var(--pink); }
  .side-slogan { position: absolute; left: 614px; top: 108px; font-size: 15px; }
  .services { list-style: none; font-size: 13.5px; line-height: 1.25; }
  .services li::before { content: "• "; }
  .side-services { position: absolute; left: 516px; top: 134px; display: grid; grid-template-columns: 190px 150px; row-gap: 2px; }

  /* rear panel */
  .rear-panel { position: absolute; left: 260px; top: 650px; width: 397px; height: 340px; background: var(--white); border-radius: 10px; }
  .rear-brand { left: 0; width: 397px; top: 82px; }
  .rear-brand .brand-name { font-size: 22px; }
  .rear-brand .brand-tagline { font-size: 9px; letter-spacing: 2px; margin-top: 3px; }
  .rear-brand .rule { width: 24px; height: 2px; }
  .rear-slogan { position: absolute; left: 0; width: 397px; top: 123px; text-align: center; font-size: 13px; }
  .rear-drips { position: absolute; left: 90px; top: 152px; width: 216px; height: 24px; border-radius: 3px 3px 12px 12px; background: linear-gradient(90deg, var(--cyan), var(--violet), var(--pink), var(--red), var(--yellow)); }
  .rear-plate { position: absolute; left: 46px; top: 226px; width: 120px; height: 32px; background: var(--panel-grey); display: flex; align-items: center; justify-content: center; font-family: "Marcellus", serif; font-size: 17px; }
  .rear-contact { position: absolute; left: 205px; top: 218px; font-size: 10.5px; line-height: 1.25; }
  .rear-contact p + p { margin-top: 6px; }
  .rear-services { position: absolute; left: 24px; top: 290px; display: grid; grid-template-columns: 204px 160px; font-size: 13px; }

  .draft-label { position: absolute; left: 14px; top: 1176px; font-size: 12px; }
</style>
</head>
<body>

  <header class="brand header-brand">
    <div class="brand-name">TEODOR FINK</div>
    <div class="brand-tagline"><span class="rule"></span>Farben - Tapeten - Putze<span class="rule"></span></div>
  </header>

  <section class="side-panel" aria-label="Seitenansicht der Folierung">
    <div class="side-blue"></div>
    <div class="side-brush" role="img" aria-label="Pinselstrich-Übergang von Blau zu Weiß"></div>
    <div class="side-drips" role="img" aria-label="Bunte herabtropfende Farbe"></div>
    <div class="side-contact">
      <div><p>Info@teodor-fink.de</p><p>0163-5550192</p></div>
      <div><p>Kerbweg 9</p><p>70899 Tannbach</p></div>
    </div>
    <span class="side-mark"></span>
    <div class="side-brand"><div class="brand-name">TEODOR<br>FINK</div></div>
    <p class="side-slogan">Qualität die man sehen kann</p>
    <ul class="services side-services">
      <li>Maler und Lackierarbeiten</li><li>Stuckateurarbeiten</li>
      <li>Bodenbelagsarbeiten</li><li>Tapezierarbeiten</li>
    </ul>
  </section>

  <section class="rear-panel" aria-label="Heckansicht der Folierung">
    <div class="brand rear-brand">
      <div class="brand-name">TEODOR FINK</div>
      <div class="brand-tagline"><span class="rule"></span>Farben - Tapeten - Putze<span class="rule"></span></div>
    </div>
    <p class="rear-slogan">Qualität die man sehen kann</p>
    <div class="rear-drips" role="img" aria-label="Bunte herabtropfende Farbe"></div>
    <div class="rear-plate">TEODOR FINK</div>
    <div class="rear-contact">
      <p>Info@teodor-fink.de<br>0163-5550192</p>
      <p>Kerbweg 9<br>70899 Tannbach</p>
    </div>
    <ul class="services rear-services">
      <li>Maler und Lackierarbeiten</li><li>Stuckateurarbeiten</li>
      <li>Bodenbelagsarbeiten</li><li>Tapezierarbeiten</li>
    </ul>
  </section>

  <p class="draft-label">Entwurf 2.0</p>

</body>
</html>
```